Ridgecrest Capital Allies need a desert themed website!

We need a web design and development for our informational website for our new company named Ridgecrest Capital Allies. We would like it to be desert themed and it can be color or black and white. We would like it to be classy and clean, while also talking to the benefits of investment partner with us.

We're thinking probably a home page with a nice image of a Scottsdale landscape, then other pages would What we offer our partners page (or other wording if you find something better), a meet the founder page, and a contact us page.

What we offer our partners (or other wording if you think of something better):
Our investors offer an opportunity to families that cannot usually get approved for a mortgage, to be able to become future homeowners. Thus, Benefiting both the investors and local surrounding community members. Our investors get to both have all the benefits of an investment with receiving above market rates of return to themselves and helping families find homes at the same time.

Maybe also build an infographic with these benefits: Safety, Security, Long-term investment horizon, cashflow, tax benefits, above market rate of return, and capital growth.

And a meet the founder page. With my headshot.

Paul Harnetti is a private equity investor providing significantly above market returns to his investment partners while taking the time to be involved with his community and family. Paul first honed his skills in taking calculated risk decisions while very young where he took on playing poker professionally. He succeeded at the highest levels for over a decade competing in high stakes professional cash games around the world.

From the poker world he transitioned to investing in public and private markets. He took an approach of knowing the companies he invests in intimately and after over 10,000 hours of research became known in his community as the person to get investment advice on the electric vehicle industry for his voracious research and expert insight.

He now invests in single family homes in the Phoenix market using his past experience analyzing probabilistic outcomes and comparing the ROIs of different potential strategies. These skills have contributed to his success in investing in companies where he used his ability to assess risk to reward ratios to significantly outperform the market over an extended period.

Contact page we want my email Paul@RidgecrestFunds.example, my instagram: @PaulHarnetti, and my linkedin https://www.profilehub.example/in/paul-harnetti-58172036/

I have included my headshot for the about me page. I've included some saguaro generated images feel free to incorporate into the website (or make them the company logo), or not, whatever you feel gives the best look for the website.

```html
<!DOCTYPE html>
<html lang="en">
<head>
<meta charset="utf-8">
<title>RidgecrestAllies</title>
<link href="https://fonts.googleapis.com/css2?family=Roboto:wght@400;500;700&display=swap" rel="stylesheet">
<style>
:root{
  --cream:#fdf8ea;
  --green:#2b4a25;
  --green-dark:#233d1e;
  --yellow:#f2c417;
  --ink:#1b1b1b;
  --muted:#5d5d5d;
  --field:#e2dccd;
  --black:#1a1a1a;
}
*{margin:0;padding:0;box-sizing:border-box}
html,body{width:1200px;height:3438px;overflow:hidden}
body{position:relative;background:var(--cream);font-family:'Roboto',Arial,sans-serif;color:var(--ink)}
.abs{position:absolute}
.topline{left:0;top:0;width:1200px;height:4px;background:var(--yellow)}
.nav{left:0;top:4px;width:1200px;height:66px;background:var(--cream);border-bottom:1px solid #ddd6c4}
.brand{left:145px;top:20px;font-size:24px;font-weight:700;color:var(--green);letter-spacing:.3px}
.menu{top:28px;font-size:14px;font-weight:500;color:var(--ink)}
.btn{display:flex;align-items:center;justify-content:center;background:var(--green);color:#fff;font-weight:500;font-size:14px;text-transform:uppercase}
.hero-photo{left:0;top:70px;width:1200px;height:630px;background:linear-gradient(180deg,#2f5ea0 0%,#6d95c6 28%,#b7b49a 46%,#a98353 62%,#8d6a3e 80%,#7a5a35 100%)}
.hero-text{left:0;width:1200px;text-align:center;color:#fff}
h2.title{font-size:34px;font-weight:700;text-transform:uppercase}
h2.title span{color:var(--yellow)}
.about-img{left:145px;top:762px;width:406px;height:391px;border:2px solid var(--green);border-radius:22px 0 22px 0;background:linear-gradient(135deg,#cfd8de,#9aa9b4 55%,#6e7f8c)}
.about-copy{left:620px;top:830px;width:435px;font-size:13.5px;line-height:24.6px;color:var(--muted);text-align:justify}
.about-copy p{margin-bottom:7px}
.benefits-bg{left:0;top:1190px;width:1200px;height:824px;background:linear-gradient(180deg,#f6ecd6 0%,#eedcb6 50%,#e4cc9c 100%)}
.icon-label{font-size:16.5px;font-weight:500;color:var(--ink)}
.founder-bg{left:0;top:2014px;width:1200px;height:506px;background:linear-gradient(180deg,#2f4c28,#3b5a30 60%,#4d6a3c)}
.founder-photo{left:742px;top:1935px;width:458px;height:585px;background:linear-gradient(160deg,#6d5647,#a88370 45%,#8a7d74 80%,#6f6f6a)}
.founder-copy{left:144px;top:2126px;width:503px;font-size:13.5px;line-height:24px;color:#fff;text-align:justify}
.founder-copy p{margin-bottom:9px}
.field{background:var(--field);border-radius:3px;font-size:13px;color:#333;padding:0 18px;display:flex;align-items:center}
.foot h4{font-size:17px;font-weight:700;color:#fff;text-transform:uppercase}
.foot-link{font-size:11.5px;color:#fff}
.foot-ico{width:24px;height:24px;border:1.5px solid var(--yellow);border-radius:50%;display:flex;align-items:center;justify-content:center}
.bottom-bar{left:0;top:3400px;width:1200px;height:38px;background:var(--green);color:#fff;font-size:12.5px}
</style>
</head>
<body>

<div class="abs topline"></div>
<header class="abs nav">
  <div class="abs brand">RIDGECRESTALLIES</div>
  <div class="abs menu" style="left:527px">HOME</div>
  <div class="abs menu" style="left:618px">ABOUT</div>
  <div class="abs menu" style="left:715px">FOUNDER</div>
  <div class="abs menu" style="left:825px">CONTACT</div>
  <div class="abs btn" style="left:930px;top:15px;width:124px;height:37px;font-size:13px">Get a Quote</div>
</header>

<section>
  <div class="abs hero-photo" role="img" aria-label="Sonoran desert landscape with saguaro cacti and mountains under a blue sky"></div>
  <svg class="abs" style="left:0;top:560px" width="1200" height="150" viewBox="0 0 1200 150">
    <path d="M0 60 C120 65 200 115 330 100 C460 85 520 15 620 18 C720 22 760 110 900 110 C1030 110 1100 70 1200 60 L1200 150 L0 150 Z" fill="var(--cream)"/>
  </svg>
  <div class="abs hero-text" style="top:174px;font-size:12px;color:var(--yellow)">Welcome To</div>
  <div class="abs hero-text" style="top:208px;font-size:40px;font-weight:700">RIDGECRESTALLIES</div>
  <div class="abs hero-text" style="top:272px;font-size:15.5px;line-height:25px;font-weight:500">Lorem ipsum dolor sit amet, consectetur adipiscing elit, sed do eiusmod<br>tempor incididunt ut labore et dolore magna aliqua.</div>
  <div class="abs btn" style="left:530px;top:348px;width:141px;height:47px;font-size:15px">Get Started</div>
</section>

<section>
  <div class="abs" style="left:117px;top:1003px;width:200px;height:177px;background:var(--yellow);border-radius:0 0 0 30px"></div>
  <div class="abs about-img" role="img" aria-label="Three business colleagues reviewing work on a laptop"></div>
  <h2 class="abs title" style="left:620px;top:772px">About <span>Us</span></h2>
  <div class="abs about-copy">
    <p>Lorem ipsum dolor sit amet, consectetur adipiscing elit, sed do eiusmod tempor incididunt ut labore et dolore magna aliqua. Ut enim ad minim veniam, quis nostrud exercitation ullamco laboris nisi ut aliquip ex ea commodo consequat. Duis aute irure dolor in reprehenderit.</p>
    <p>Duis aute irure dolor in reprehenderit in voluptate velit esse cillum dolore eu fugiat nulla pariatur. Excepteur sint occaecat cupidatat non proident, sunt in culpa qui officia deserunt mollit anim id est laborum. Nemo enim ipsam voluptatem quia voluptas sit aspernatur aut odit aut fugit, sed quia consequuntur magni dolores eos qui ratione voluptatem.</p>
  </div>
  <div class="abs btn" style="left:620px;top:1083px;width:133px;height:42px">Learn More</div>
</section>

<section>
  <div class="abs benefits-bg" role="img" aria-label="Faded desert scene with saguaro cactus and distant hills"></div>
  <svg class="abs" style="left:0;top:1180px" width="1200" height="110" viewBox="0 0 1200 110">
    <path d="M0 0 H1200 V30 C1050 5 900 0 760 20 C600 45 450 80 300 95 C170 105 80 80 0 40 Z" fill="var(--cream)"/>
  </svg>
  <h2 class="abs title" style="left:0;width:1200px;text-align:center;top:1307px"><span>Our</span> Benefits</h2>

  <svg class="abs" style="left:0;top:1380px" width="1200" height="540" viewBox="0 1380 1200 540">
    <g stroke="var(--yellow)" stroke-width="2.5">
      <line x1="537" y1="1541" x2="515" y2="1495"/>
      <line x1="655" y1="1532" x2="673" y2="1490"/>
      <line x1="719" y1="1603" x2="767" y2="1603"/>
      <line x1="705" y1="1712" x2="745" y2="1738"/>
      <line x1="617" y1="1765" x2="618" y2="1812"/>
      <line x1="523" y1="1732" x2="485" y2="1765"/>
      <line x1="483" y1="1631" x2="436" y2="1631"/>
    </g>
    <circle cx="605" cy="1648" r="123" fill="var(--green)"/>
    <circle cx="605" cy="1648" r="97" fill="#fff"/>
    <circle cx="605" cy="1648" r="91" fill="#b2502d" role="img" aria-label="Red rock desert butte at sunset"/>
    <g fill="var(--yellow)" stroke="#fff" stroke-width="2">
      <circle cx="537" cy="1541" r="6"/><circle cx="655" cy="1532" r="6"/><circle cx="719" cy="1603" r="6"/>
      <circle cx="705" cy="1712" r="6"/><circle cx="617" cy="1765" r="6"/><circle cx="523" cy="1732" r="6"/><circle cx="483" cy="1631" r="6"/>
    </g>
    <g fill="#fff" stroke="var(--green)" stroke-width="9">
      <circle cx="497" cy="1455" r="44"/><circle cx="692" cy="1445" r="44"/><circle cx="813" cy="1604" r="44"/>
      <circle cx="784" cy="1763" r="44"/><circle cx="620" cy="1858" r="44"/><circle cx="455" cy="1795" r="44"/><circle cx="388" cy="1632" r="44"/>
    </g>
    <g fill="none" stroke="var(--green)" stroke-width="2" stroke-linecap="round" stroke-linejoin="round">
      <path d="M487 1440 h20 l-4 -6 h-12 z M483 1468 c0 -14 8 -26 14 -28 c6 2 14 14 14 28 z M493 1460 h8 M497 1448 v16"/>
      <path d="M692 1428 l14 5 v9 c0 8 -6 14 -14 17 c-8 -3 -14 -9 -14 -17 v-9 z M686 1444 l5 5 l9 -9 M674 1462 h10 l10 4 h14"/>
      <path d="M813 1584 l18 6 v12 c0 10 -8 18 -18 22 c-10 -4 -18 -12 -18 -22 v-12 z M804 1604 l7 7 l12 -13"/>
      <path d="M766 1770 l28 -22 M794 1748 h-10 M794 1748 v10 M802 1756 l-28 22 M774 1778 h10 M774 1778 v-10"/>
      <circle cx="784" cy="1763" r="9"/>
      <circle cx="620" cy="1858" r="16"/><path d="M620 1850 v16 M615 1854 h8 M615 1862 h8 M600 1848 l6 -6 M640 1868 l-6 6"/>
      <path d="M455 1775 l6 4 h7 l2 7 l5 5 l-3 6 l3 6 l-5 5 l-2 7 h-7 l-6 4 l-6 -4 h-7 l-2 -7 l-5 -5 l3 -6 l-3 -6 l5 -5 l2 -7 h7 z M448 1796 l5 5 l9 -10"/>
      <path d="M370 1648 v-14 h10 v14 M382 1648 v-22 h10 v22 M394 1648 v-8 M366 1648 h38 M390 1620 v-12 M384 1614 l6 -6 l6 6"/>
      <circle cx="402" cy="1640" r="8"/>
    </g>
  </svg>
  <div class="abs icon-label" style="left:379px;top:1442px">Capital</div>
  <div class="abs icon-label" style="left:759px;top:1437px">Safety</div>
  <div class="abs icon-label" style="left:879px;top:1594px">Security</div>
  <div class="abs icon-label" style="left:846px;top:1754px">Cashflow</div>
  <div class="abs icon-label" style="left:505px;top:1921px">Long-term investment horizon</div>
  <div class="abs icon-label" style="left:295px;top:1794px">Tax Benefits</div>
  <div class="abs icon-label" style="left:179px;top:1609px;text-align:right;width:143px;line-height:25px">Above Market Rate Of Return</div>
</section>

<section>
  <div class="abs founder-bg"></div>
  <div class="abs founder-photo" role="img" aria-label="Headshot of founder Paul Harnetti"></div>
  <h2 class="abs title" style="left:143px;top:2070px;color:#fff">Meet the <span>Founder</span></h2>
  <div class="abs founder-copy">
    <p>Paul Harnetti is a private equity investor providing significantly above market returns to his investment partners while taking the time to be involved with his community and family. Paul first honed his skills in taking calculated risk decisions while very young where he took on playing poker professionally.</p>
    <p>He succeeded at the highest levels for over a decade competing in high stakes professional cash games around the world.From the poker world he transitioned to investing in public and private markets. He took an approach of knowing the companies he invests in intimately and after over 10,000 hours of research became known in his community as the person to get investment advice on the electric vehicle industry for his voracious research and expert insight.</p>
  </div>
  <div class="abs btn" style="left:144px;top:2402px;width:133px;height:42px;background:var(--cream);color:var(--green)">Learn More</div>
  <svg class="abs" style="left:0;top:2485px" width="1200" height="45" viewBox="0 0 1200 45">
    <path d="M0 20 C200 30 400 5 600 12 C800 18 1000 5 1200 15 V45 H0 Z" fill="#c9c7b3"/>
    <path d="M0 30 C220 38 420 16 620 22 C820 28 1020 18 1200 26 V45 H0 Z" fill="var(--cream)"/>
  </svg>
</section>

<section>
  <h2 class="abs title" style="left:0;width:1200px;text-align:center;top:2588px">Contact <span>Us</span></h2>
  <div class="abs field" style="left:186px;top:2667px;width:401px;height:46px">Name</div>
  <div class="abs field" style="left:186px;top:2728px;width:401px;height:46px">Email Address</div>
  <div class="abs field" style="left:186px;top:2789px;width:401px;height:46px">Phone Number</div>
  <div class="abs field" style="left:610px;top:2666px;width:405px;height:172px;align-items:flex-start;padding-top:16px">Message</div>
  <svg class="abs" style="left:189px;top:2884px" width="18" height="14" viewBox="0 0 18 14"><rect width="18" height="14" rx="2" fill="var(--yellow)"/><path d="M1 2 l8 6 l8 -6" stroke="#fff" stroke-width="1.6" fill="none"/></svg>
  <div class="abs" style="left:214px;top:2880px;font-size:18px;color:var(--ink)">Paul@RidgecrestFunds.example</div>
  <div class="abs btn" style="left:532px;top:2873px;width:136px;height:39px;font-size:13px">Submit Now</div>
  <div class="abs" style="left:851px;top:2880px;font-size:21px;font-weight:500">Follow Us : <span style="color:var(--yellow);font-size:17px">@PaulHarnetti</span></div>
</section>

<footer class="foot">
  <svg class="abs" style="left:0;top:2990px" width="1200" height="420" viewBox="0 0 1200 420">
    <path d="M0 60 C100 75 180 40 280 70 C380 100 450 140 560 130 C680 120 740 40 900 30 C1020 22 1100 35 1200 20 V420 H0 Z" fill="var(--black)"/>
  </svg>

  <h4 class="abs" style="left:143px;top:3174px">Quick Links</h4>
  <div class="abs foot-link" style="left:146px;top:3212px">Home</div>
  <div class="abs foot-link" style="left:146px;top:3236px">About</div>
  <div class="abs foot-link" style="left:146px;top:3260px">Founder</div>
  <div class="abs foot-link" style="left:146px;top:3284px">Contact</div>

  <h4 class="abs" style="left:445px;top:3174px">Contact Us</h4>
  <div class="abs foot-ico" style="left:445px;top:3213px"><svg width="12" height="12" viewBox="0 0 12 12"><path d="M2 1 l3 0 l1 3 l-2 1 c1 2 2 3 4 4 l1 -2 l3 1 v3 c-6 0 -10 -4 -10 -10 z" fill="var(--yellow)"/></svg></div>
  <div class="abs foot-link" style="left:479px;top:3218px">+1-888-888-8888</div>
  <div class="abs foot-ico" style="left:445px;top:3254px"><svg width="12" height="9" viewBox="0 0 12 9"><rect width="12" height="9" rx="1" fill="var(--yellow)"/><path d="M1 1 l5 4 l5 -4" stroke="var(--black)" stroke-width="1.2" fill="none"/></svg></div>
  <div class="abs foot-link" style="left:479px;top:3259px">Paul@RidgecrestFunds.example,</div>
  <div class="abs foot-ico" style="left:445px;top:3295px"><svg width="10" height="13" viewBox="0 0 10 13"><path d="M5 13 c-3 -4 -5 -6 -5 -8 a5 5 0 0 1 10 0 c0 2 -2 4 -5 8 z" fill="var(--yellow)"/><circle cx="5" cy="5" r="2" fill="var(--black)"/></svg></div>
  <div class="abs foot-link" style="left:479px;top:3300px">Lorem ipsum dolor sit amet, 651</div>

  <h4 class="abs" style="left:814px;top:3174px">Subscribe to our Blog</h4>
  <div class="abs foot-link" style="left:815px;top:3207px;font-size:11px">Lorem ipsum dolor sit amet, consectetur.</div>
  <div class="abs" style="left:815px;top:3239px;width:191px;height:34px;background:#fff;font-size:10px;color:#777;display:flex;align-items:center;padding-left:14px">✉&nbsp; Email Address</div>
  <div class="abs btn" style="left:1006px;top:3239px;width:44px;height:34px"><svg width="16" height="14" viewBox="0 0 16 14"><path d="M0 7 L16 0 L12 14 L8 9 Z" fill="#fff"/></svg></div>

  <div class="abs bottom-bar">
    <div class="abs" style="left:143px;top:12px">Copyright© <u>2024 Ridgecrestallies</u> &nbsp;|&nbsp; All Rights Reserved</div>
    <div class="abs" style="left:824px;top:12px">Terms and Conditions &nbsp; | &nbsp; Privacy Policy</div>
  </div>
</footer>

</body>
</html>
```